Business / Stationery Design Project

Hi,

I need business cards and all other stationary designed for my new finance broking business.

Stationary required:

Business card
Letter head
with compliments
envelopes

There is gold in the logo design so some gold would be good and open to other creative ideas / colours.

Regards
Milo
Updates

Target Market(s)

Small to medium business customers. Also to appeal to referrers who include accounting firms and other associated professionals (valuers etc)

Industry/Entity Type

Finance

Requirements
Must have
• Professional, classy look.

```html
<!DOCTYPE html>
<html lang="en">
<head>
<meta charset="utf-8">
<title>Harwell Finance Stationery</title>
<link href="https://fonts.googleapis.com/css2?family=Open+Sans:wght@400;600;700&family=Great+Vibes&display=swap" rel="stylesheet">
<style>
  :root{
    --backdrop:#ececec;
    --paper:#ffffff;
    --charcoal:#3a3937;
    --gold:#c9a460;
    --ink:#3c3c3c;
    --muted:#6b6b6b;
  }
  *{box-sizing:border-box;margin:0;padding:0}
  html,body{width:1200px;height:795px;overflow:hidden;background:var(--backdrop);font-family:"Open Sans",Arial,sans-serif;color:var(--ink)}
  .canvas{position:relative;width:1200px;height:795px}

  /* Letterhead */
  .letterhead{position:absolute;left:70px;top:45px;width:500px;height:707px;background:var(--paper);box-shadow:0 2px 10px rgba(0,0,0,.08)}
  .letterhead__band{display:flex;height:9px}
  .letterhead__band-gold{width:36%;background:var(--gold)}
  .letterhead__band-dark{flex:1;background:var(--charcoal)}
  .brand{display:flex;align-items:center;gap:6px;font-weight:600;letter-spacing:.14em;text-transform:uppercase;color:var(--charcoal)}
  .brand__dot{width:8px;height:8px;border-radius:50%;background:var(--gold)}
  .letterhead .brand{position:absolute;left:42px;top:50px;font-size:13px}
  .letterhead__address{position:absolute;left:210px;top:44px;font-size:6.5px;line-height:1.45;color:var(--muted)}
  .contact-list{list-style:none;font-size:6.5px;line-height:1.5;color:var(--muted)}
  .contact-list b{display:inline-block;width:9px;color:var(--gold);font-weight:700}
  .letterhead .contact-list{position:absolute;left:360px;top:44px}
  .letter{position:absolute;left:70px;top:128px;width:370px;font-size:8px;line-height:1.55;color:var(--muted)}
  .letter__greeting{font-weight:700;color:var(--ink);margin-bottom:8px}
  .letter p{margin-bottom:9px}
  .signature{position:absolute;left:72px;top:470px}
  .signature__name{font-family:"Great Vibes",cursive;font-size:30px;color:var(--charcoal);line-height:1}
  .signature__role{font-size:8px;font-weight:700;color:var(--ink)}

  /* Business cards */
  .card{position:absolute;left:660px;width:470px;height:268px;box-shadow:0 2px 10px rgba(0,0,0,.1)}
  .card--front{top:80px;background:var(--charcoal);color:#fff}
  .card--front .brand{position:absolute;right:40px;top:100px;font-size:22px;color:#fff}
  .card--front .brand__dot{width:14px;height:14px}
  .card__web{position:absolute;right:40px;top:140px;font-size:10px;letter-spacing:.05em;color:#ddd}
  .card--back{top:450px;background:var(--paper)}
  .card--back .brand{position:absolute;right:34px;top:34px;font-size:16px}
  .card__name{position:absolute;left:34px;top:96px;background:var(--gold);color:#fff;font-size:15px;padding:3px 10px}
  .card--back .contact-list{position:absolute;left:38px;top:134px;font-size:8.5px}
  .card--back .contact-list b{width:12px}
  .card__address{position:absolute;left:38px;top:196px;font-size:8.5px;line-height:1.45;color:var(--muted)}
</style>
</head>
<body>
<main class="canvas">

  <section class="letterhead" aria-label="Letterhead">
    <div class="letterhead__band"><span class="letterhead__band-gold"></span><span class="letterhead__band-dark"></span></div>
    <div class="brand"><span class="brand__dot"></span>Harwell Finance</div>
    <address class="letterhead__address">
      Harwell Finance PTY LTD<br>ABN 12 345 678 901<br>Suite 4 / 18 Linden Ave<br>Maple Hill NSW 2150<br>Australia
    </address>
    <ul class="contact-list">
      <li><b>P</b>+61 (02) 9000 1234</li>
      <li><b>F</b>+61 (02) 9000 1235</li>
      <li><b>M</b>+61 0400 123 456</li>
      <li><b>E</b>info@harwellfinance.com.au</li>
      <li><b>W</b>www.harwellfinance.com.au</li>
    </ul>
    <article class="letter">
      <p class="letter__greeting">Lorem Ipsum,</p>
      <p>Cras mattis consectetur purus sit amet fermentum. Etiam porta sem malesuada magna mollis euismod. Integer posuere erat a ante venenatis dapibus posuere velit aliquet. Cras justo odio, dapibus ac facilisis in, egestas eget quam. Aenean eu leo quam. Pellentesque ornare sem lacinia quam venenatis vestibulum.</p>
      <p>Vivamus sagittis lacus vel augue laoreet rutrum faucibus dolor auctor. Donec sed odio dui. Etiam porta sem malesuada magna mollis euismod. Morbi leo risus, porta ac consectetur ac, vestibulum at eros. Nullam id dolor id nibh ultricies vehicula ut id elit.</p>
      <p>Donec id elit non mi porta gravida at eget metus. Fusce dapibus, tellus ac cursus commodo, tortor mauris condimentum nibh, ut fermentum massa justo sit amet risus. Cras justo odio, dapibus ac facilisis in, egestas eget quam. Cum sociis natoque penatibus et magnis dis parturient montes, nascetur ridiculus mus.</p>
      <p>Cum sociis natoque penatibus et magnis dis parturient montes, nascetur ridiculus mus. Curabitur blandit tempus porttitor. Aenean lacinia bibendum nulla sed consectetur. Lorem ipsum dolor sit amet, consectetur adipiscing elit.</p>
      <p>Cras justo odio, dapibus ac facilisis in, egestas eget quam. Morbi leo risus, porta ac consectetur ac, vestibulum at eros. Duis mollis, est non commodo luctus, nisi erat porttitor ligula, eget lacinia odio sem nec elit. Integer posuere erat a ante venenatis dapibus posuere velit aliquet. Vivamus sagittis lacus vel augue laoreet rutrum faucibus dolor auctor.</p>
    </article>
    <div class="signature">
      <div class="signature__name">Your Name</div>
      <div class="signature__role">Company Director</div>
    </div>
  </section>

  <section class="card card--front" aria-label="Business card front">
    <div class="brand"><span class="brand__dot"></span>Harwell Finance</div>
    <div class="card__web">www.harwellfinance.com.au</div>
  </section>

  <section class="card card--back" aria-label="Business card back">
    <div class="brand"><span class="brand__dot"></span>Harwell Finance</div>
    <div class="card__name">Greg Milo</div>
    <ul class="contact-list">
      <li><b>P</b>+61 (02) 9000 1234</li>
      <li><b>M</b>+61 0400 123 456</li>
      <li><b>E</b>greg@harwellfinance.com.au</li>
    </ul>
    <address class="card__address">
      Harwell Finance PTY LTD<br>Suite 4 / 18 Linden Ave<br>Maple Hill NSW 2150<br>Australia
    </address>
  </section>

</main>
</body>
</html>
```